Pinecrest 71 Studios needs a web design

We need a website design for a California based visual effects (VFX) company to show potential clients and employees who we are and what we do. We are currently focusing on compositing based tasks such as but not limited to multi-pass composites, green screen extraction, rotoscope, paint fixes and retimes. We like imagery that makes people think of 'California' such as the state flag, sunshine and the beach. The website should send a message that although we are a new company, we are not new to the vfx industry. The website needs to be compatible with mobile devices. We also need the ability to edit and modify the site.

Target Market(s)

Studio executive, producers and potential employees.

Industry/Entity Type

Flag

Coding

Coded - Design and coding required

Number of Pages Required

4 page

Font styles to use
Serif
Sans Serif

Requirements
Must have
• Must have space for company and individual biographies. Must have a page for a credits list and show reel. Must also have space for contact info ex. maps, email, social media.

```html
<!DOCTYPE html>
<html lang="en">
<head>
<meta charset="utf-8">
<title>Pinecrest 71 Studios</title>
<link rel="stylesheet" href="https://fonts.googleapis.com/css2?family=Open+Sans:wght@300;400&family=Oswald:wght@400&family=Tinos&display=swap">
<style>
  :root {
    --ink: #0b0b0b;
    --page: #e4e0e4;
    --red: #a31417;
    --red-dark: #8c1013;
    --text: #7a7a7a;
    --heading: #5e5e5e;
    --white: #ffffff;
    --footer-text: #9a9a9a;
    --sky-top: #6f7178;
    --sky-mid: #a7a8ad;
    --sand: #8a8580;
  }
  * { box-sizing: border-box; margin: 0; padding: 0; }
  html, body { width: 1153px; height: 1200px; overflow: hidden; }
  body {
    position: relative;
    background: var(--page);
    font-family: "Open Sans", Arial, sans-serif;
    color: var(--text);
  }
  .topbar {
    position: absolute; left: 0; top: 0; width: 1153px; height: 28px;
    background: var(--ink);
  }
  .topbar__sitemap {
    position: absolute; left: 64px; top: 7px;
    font-size: 11px; color: var(--white);
  }
  .topbar__social {
    position: absolute; right: 56px; top: 0; display: flex; height: 28px;
  }
  .topbar__social span {
    width: 28px; height: 28px; border-left: 1px solid #333;
    display: flex; align-items: center; justify-content: center;
  }
  .topbar__social span:last-child { border-right: 1px solid #333; }
  .topbar__social i {
    display: block; width: 10px; height: 10px; background: var(--white);
  }
  .header {
    position: absolute; left: 0; top: 28px; width: 1153px; height: 186px;
  }
  .brand {
    position: absolute; left: 58px; top: 66px;
    display: flex; align-items: center; gap: 10px;
    font-family: "Open Sans", Arial, sans-serif; font-weight: 400;
    font-size: 20px; color: var(--ink);
  }
  .brand__dot {
    width: 22px; height: 22px; border-radius: 50%; background: var(--red);
  }
  .header__tagline {
    position: absolute; right: 52px; top: 118px;
    font-family: "Tinos", "Times New Roman", serif;
    font-size: 30px; color: var(--ink);
  }
  .nav {
    position: absolute; left: 0; top: 214px; width: 1153px; height: 47px;
    background: var(--red);
    border-bottom: 2px solid var(--red-dark);
    display: flex; align-items: center; padding-left: 58px;
  }
  .nav a {
    font-family: "Oswald", Arial, sans-serif; font-size: 12px;
    text-transform: uppercase; color: var(--white); text-decoration: none;
    padding: 0 12px; border-right: 1px solid #c44;
    line-height: 16px;
  }
  .nav a:first-child { padding-left: 12px; color: #2a0000; }
  .nav .caret { font-size: 9px; margin-left: 3px; }
  .nav__rule {
    position: absolute; left: 0; top: 261px; width: 780px; height: 4px;
    background: #a9a6aa;
  }
  .banner {
    position: absolute; left: 0; top: 265px; width: 1153px; height: 359px;
    background: linear-gradient(180deg, var(--sky-top) 0%, var(--sky-mid) 45%, #b9b4ad 62%, var(--sand) 100%);
  }
  .welcome {
    position: absolute; left: 0; top: 636px; width: 1153px;
    display: flex; justify-content: center; align-items: center; gap: 8px;
  }
  .welcome__icon {
    width: 45px; height: 45px; border-radius: 50%; background: var(--red);
    display: flex; align-items: center; justify-content: center;
  }
  .welcome h1 {
    font-weight: 300; font-size: 33px; color: var(--heading);
    text-transform: uppercase; letter-spacing: -0.5px;
  }
  .feature-mark {
    position: absolute; left: 124px; top: 724px; width: 366px; height: 406px;
    display: flex; flex-direction: column; align-items: center; justify-content: center; gap: 22px;
    font-size: 34px; font-weight: 400; color: var(--ink); text-align: center;
  }
  .feature-mark__dot {
    width: 40px; height: 40px; border-radius: 50%; background: var(--red);
  }
  .about {
    position: absolute; left: 589px; top: 724px; width: 510px;
    font-weight: 300; font-size: 19.6px; line-height: 23.6px; color: var(--text);
  }
  .about p + p { margin-top: 8px; }
  .footer__rule {
    position: absolute; left: 0; top: 1159px; width: 1153px; height: 6px;
    background: var(--red);
  }
  .footer {
    position: absolute; left: 0; top: 1165px; width: 1153px; height: 35px;
    background: var(--ink);
  }
  .footer__copy {
    position: absolute; left: 55px; top: 10px; font-size: 11px; color: var(--footer-text);
  }
  .to-top {
    position: absolute; left: 1104px; top: 1151px; width: 43px; height: 43px;
    background: #2c2c2c; display: flex; align-items: center; justify-content: center;
  }
</style>
</head>
<body>
  <div class="topbar">
    <span class="topbar__sitemap">SiteMap</span>
    <div class="topbar__social">
      <span><i></i></span><span><i></i></span><span><i></i></span><span><i></i></span><span><i></i></span>
    </div>
  </div>

  <header class="header">
    <div class="brand"><span class="brand__dot"></span>Pinecrest 71 Studios</div>
    <div class="header__tagline">Pinecrest 71 Visual Effects Studios</div>
  </header>

  <nav class="nav">
    <a href="#">Home</a>
    <a href="#">Blog<span class="caret">&#8964;</span></a>
    <a href="#">Client Portfolio<span class="caret">&#8964;</span></a>
    <a href="#">Team</a>
    <a href="#">Menu Item<span class="caret">&#8964;</span></a>
    <a href="#">Contact</a>
  </nav>
  <div class="nav__rule"></div>

  <div class="banner" role="img" aria-label="Beachfront homes and tall palm trees along a sandy California shore under a cloudy sky"></div>

  <div class="welcome">
    <div class="welcome__icon">
      <svg width="22" height="14" viewBox="0 0 22 14" aria-hidden="true">
        <rect x="0" y="1" width="14" height="12" rx="2" fill="#fff"/>
        <polygon points="14,7 22,1 22,13" fill="#fff"/>
      </svg>
    </div>
    <h1>Welcome to Pinecrest 71 Studios</h1>
  </div>

  <div class="feature-mark">
    <span class="feature-mark__dot"></span>
    <span>Pinecrest 71 Studios</span>
  </div>

  <section class="about">
    <p>Formed in 2014, Pinecrest 71 Studios is a visual effects studio based in Playa Serena, CA. Taking their name from early Californian history, Pinecrest 71 Studios looks to continue the Golden State’s tradition of strong and reliable visual effects. With close to 20 years in the vfx community, Pinecrest 71 Studios has the ability to service feature films, television, and commercials. Pinecrest 71’s capabilities are focused on compositing, 2.5D effects and environments, rotoscope, paint fixes, color timing and other 2D tasks.</p>
    <p>With a network of talented acquaintances built over the years, Pinecrest 71 Studios can adapt to the clients needs. At a time when budgets and schedules are shrinking Pinecrest 71 Studios’ goal is supplying world class visual effects work on a workable budget.</p>
  </section>

  <div class="footer__rule"></div>
  <footer class="footer">
    <span class="footer__copy">Copyright © 2015 Pinecrest 71 Studios. All rights reserved.</span>
  </footer>
  <div class="to-top">
    <svg width="26" height="14" viewBox="0 0 26 14" aria-hidden="true">
      <polyline points="1,13 13,2 25,13" fill="none" stroke="#fff" stroke-width="2"/>
    </svg>
  </div>
</body>
</html>
```